Business Card Design for Portrait photography professional

We are a small company specializing in portrait photography (weddings, family, couples, children, newborn, pregnant, etc.) Occasionally we do business portraits too and do some other type of photography. We need a business card which would fit into the same look and feel as our website theme (lumvika.com - under construction currently).
Our target customer base lies within mid- to upmarket. We want our business cards to convey a feeling of quality, solidness and a bit luxury.
Design should be universal and usable on 85mmx55mm, 90mmx50mm and 90mmx55mm
one extra file (PSD of a website didn't fit into the allowed updoad, therefore has put it into my filecrate: https://www.filecrate-example.net/s/qt7wk2rbvx9dmhe/website%20theme%20PSD.psd)

Target Market(s)

mostly private people, 25-60 years old, mostly well established.

Industry/Entity Type

Portrait Photography

Requirements
Must have
• 2 sided design (print on both sides of the business card).
Must include:
business name, logo, URL (lumvika.no) , employee name, email address, and phone number.
Colorscheme of the website lumvika.no / lumvika.com

```html
<!DOCTYPE html>
<html lang="en">
<head>
<meta charset="utf-8">
<title>Lumvika business card</title>
<link rel="stylesheet" href="https://fonts.googleapis.com/css2?family=Open+Sans:wght@400;700&display=swap">
<style>
  :root {
    --backdrop: #dcdce2;
    --card: #2b2a28;
    --ink: #f2f0ea;
    --ink-soft: #d9d6cf;
    --rule: #8d8b86;
  }
  * { margin: 0; padding: 0; box-sizing: border-box; }
  html, body { width: 1200px; height: 987px; overflow: hidden; }
  body {
    background: var(--backdrop);
    font-family: "Open Sans", Arial, sans-serif;
    color: var(--ink);
    position: relative;
  }
  .card {
    position: absolute;
    width: 540px;
    height: 350px;
    background: var(--card);
    border-radius: 30px;
  }
  .card--front { left: 50px; top: 318px; }
  .card--back  { left: 610px; top: 318px; }

  .brand-mark {
    position: absolute;
    left: 50%;
    transform: translateX(-50%);
    border: 3px solid var(--ink);
    border-radius: 50%;
    display: flex;
    align-items: center;
    justify-content: center;
  }
  .brand-mark__name {
    font-weight: 700;
    color: var(--ink);
    letter-spacing: 1px;
  }
  .card--front .brand-mark { top: 30px; width: 130px; height: 130px; }
  .card--front .brand-mark__name { font-size: 24px; }
  .card--back .brand-mark { top: 60px; width: 170px; height: 170px; }
  .card--back .brand-mark__name { font-size: 30px; }

  .staff {
    position: absolute;
    top: 178px;
    width: 100%;
    text-align: center;
    font-size: 24px;
  }
  .staff__name { font-weight: 700; }
  .staff__title { font-weight: 400; }

  .contact {
    position: absolute;
    width: 100%;
    display: flex;
    justify-content: center;
    gap: 26px;
    font-size: 18px;
    color: var(--ink-soft);
  }
  .contact--phone { top: 222px; }
  .contact--web { top: 252px; }
  .contact__item { display: flex; align-items: center; gap: 7px; }
  .contact__icon { width: 15px; height: 15px; fill: var(--ink-soft); }

  .rule {
    position: absolute;
    left: 40px;
    right: 40px;
    top: 306px;
    height: 2px;
    background: linear-gradient(90deg, transparent, var(--rule) 20%, var(--rule) 80%, transparent);
  }

  .site-url {
    position: absolute;
    top: 262px;
    width: 100%;
    text-align: center;
    font-size: 19px;
    letter-spacing: 5px;
    color: var(--ink-soft);
  }
</style>
</head>
<body>
  <section class="card card--front">
    <div class="brand-mark"><span class="brand-mark__name">lumvika</span></div>
    <p class="staff"><span class="staff__name">employee name,</span> <span class="staff__title">Title</span></p>
    <div class="contact contact--phone">
      <span class="contact__item">
        <svg class="contact__icon" viewBox="0 0 16 16" aria-hidden="true"><path d="M3.5 1l2.5 3-1.5 1.8c.8 2 2.2 3.4 4.2 4.2L10.5 8.5l3 2.5-1.2 2.6C8 14 2 8 2.4 3.2z"/></svg>
        123-456-0789
      </span>
    </div>
    <div class="contact contact--web">
      <span class="contact__item">
        <svg class="contact__icon" viewBox="0 0 16 16" aria-hidden="true"><path d="M1 3h14v10H1zM2 4.2v.4l6 4 6-4v-.4z"/></svg>
        info@lumvika.com
      </span>
      <span class="contact__item">
        <svg class="contact__icon" viewBox="0 0 16 16" aria-hidden="true"><circle cx="8" cy="8" r="6.5" fill="none" stroke="#d9d6cf" stroke-width="1.5"/><path d="M1.5 8h13M8 1.5c-3 3.5-3 9.5 0 13M8 1.5c3 3.5 3 9.5 0 13" fill="none" stroke="#d9d6cf" stroke-width="1.2"/></svg>
        www.lumvika.com
      </span>
    </div>
    <div class="rule"></div>
  </section>

  <section class="card card--back">
    <div class="brand-mark"><span class="brand-mark__name">lumvika</span></div>
    <p class="site-url">www.lumvika.com</p>
  </section>
</body>
</html>
```